Card Design for my dog training business Rustpaw Obedience

Need a business card design for my dog training business with my new logo. Want the card to come off professional yet fun. Want it to be very eye catchy as well. I normally have these at vet clinics, pet stores, and groomers. so need it to look better than my competitors.
Target Market(s)
dog owners
Industry/Entity Type
Dog Training
Contact Information for Business Card
needs logo, my name and info
Font styles to use
Serif
Colors
0255a3
ffffff
ec1f27
000000
333333
fbfbfb
Requirements
Must have
- Rustpaw Obedience
- Hollis Brandt
- 415 903 2267
- info@rustpawobedience.example
- www.rustpawobedience.example

```html
<!DOCTYPE html>
<html lang="en">
<head>
<meta charset="utf-8">
<title>Rustpaw Obedience – Business Card</title>
<link rel="stylesheet" href="https://fonts.googleapis.com/css2?family=Cinzel:wght@600&family=EB+Garamond:ital,wght@0,500;0,600;1,400&display=swap">
<style>
  :root {
    --page-bg: #f3f3f3;
    --page-edge: #e4e4e4;
    --card-white: #ffffff;
    --card-dark: #333333;
    --ink: #333333;
    --ink-soft: #555555;
    --text-light: #ffffff;
    --card-line: #dcdcdc;
  }
  * { box-sizing: border-box; margin: 0; padding: 0; }
  html, body { width: 1200px; height: 801px; overflow: hidden; }
  body {
    background: radial-gradient(ellipse at 50% 50%, var(--card-white) 0%, var(--page-bg) 55%, var(--page-edge) 100%);
    position: relative;
    font-family: "EB Garamond", Georgia, serif;
    color: var(--ink);
  }
  .card {
    position: absolute;
    top: 255px;
    width: 500px;
    height: 290px;
    border-radius: 18px;
    overflow: hidden;
    background: var(--card-white);
    border: 1px solid var(--card-line);
    box-shadow: 0 6px 18px rgba(0,0,0,0.12);
  }
  .card--front { left: 60px; }
  .card--back { left: 640px; }

  .brand {
    font-family: "EB Garamond", Georgia, serif;
    font-weight: 500;
    color: var(--ink);
    text-align: center;
    letter-spacing: 0.5px;
    line-height: 1.05;
  }
  .tagline {
    font-style: italic;
    font-weight: 400;
    color: var(--ink-soft);
    text-align: center;
  }

  .card--front .brand-block {
    position: absolute; left: 0; right: 0; top: 92px;
    display: flex; flex-direction: column; align-items: center;
  }
  .card--front .brand-mark {
    width: 14px; height: 14px; border-radius: 50%;
    background: var(--ink); margin-bottom: 12px;
  }
  .card--front .brand { font-size: 34px; }
  .card--front .tagline {
    position: absolute; left: 0; right: 0; top: 222px; font-size: 12.5px;
  }

  .back-identity {
    position: absolute; left: 0; top: 0; width: 196px; height: 100%;
    display: flex; flex-direction: column; align-items: center; justify-content: center;
    padding: 0 14px;
  }
  .back-identity .brand-mark {
    width: 11px; height: 11px; border-radius: 50%;
    background: var(--ink); margin-bottom: 10px;
  }
  .back-identity .brand { font-size: 22px; }
  .back-identity .tagline { font-size: 9.5px; margin-top: 22px; }

  .stripe-thin {
    position: absolute; top: 0; bottom: 0; left: 210px; width: 9px;
    background: var(--card-dark);
  }
  .dark-panel {
    position: absolute; top: 0; bottom: 0; left: 226px; right: 0;
    background: var(--card-dark);
    color: var(--text-light);
  }
  .holder-name {
    position: absolute; left: 42px; top: 56px;
    font-family: "Cinzel", "Times New Roman", serif;
    font-weight: 600; font-size: 17px; letter-spacing: 1px;
    white-space: nowrap;
  }
  .contact-list {
    position: absolute; left: 42px; right: 14px; top: 180px;
    list-style: none;
    font-size: 12.5px; font-weight: 600; line-height: 1;
  }
  .contact-list li {
    display: flex; align-items: center; gap: 8px; margin-bottom: 8px;
    white-space: nowrap;
  }
  .contact-icon { width: 11px; height: 11px; flex: none; }
</style>
</head>
<body>

<section class="card card--front" aria-label="Card front">
  <div class="brand-block">
    <span class="brand-mark"></span>
    <p class="brand">Rustpaw Obedience</p>
  </div>
  <p class="tagline">“Training dogs across Texas one dog at a time.”</p>
</section>

<section class="card card--back" aria-label="Card back">
  <div class="back-identity">
    <span class="brand-mark"></span>
    <p class="brand">Rustpaw Obedience</p>
    <p class="tagline">“Training dogs across Texas one dog at a time.”</p>
  </div>
  <div class="stripe-thin"></div>
  <div class="dark-panel">
    <h1 class="holder-name">HOLLIS BRANDT</h1>
    <ul class="contact-list">
      <li>
        <svg class="contact-icon" viewBox="0 0 12 12" aria-hidden="true">
          <circle cx="6" cy="6" r="6" fill="#ffffff"/>
          <path d="M4 3.2 L5 3 L5.6 4.6 L4.9 5.2 Q5.5 6.5 6.8 7.1 L7.4 6.4 L9 7 L8.8 8 Q8.4 8.9 7.4 8.7 Q4.2 7.8 3.3 4.6 Q3.1 3.6 4 3.2 Z" fill="#333333"/>
        </svg>
        <span>415 903 2267</span>
      </li>
      <li>
        <svg class="contact-icon" viewBox="0 0 12 12" aria-hidden="true">
          <circle cx="6" cy="6" r="6" fill="#ffffff"/>
          <rect x="3" y="4" width="6" height="4.2" fill="none" stroke="#333333" stroke-width="0.9"/>
          <path d="M3 4 L6 6.4 L9 4" fill="none" stroke="#333333" stroke-width="0.9"/>
        </svg>
        <span>info@rustpawobedience.example</span>
      </li>
      <li>
        <svg class="contact-icon" viewBox="0 0 12 12" aria-hidden="true">
          <circle cx="6" cy="6" r="6" fill="#ffffff"/>
          <circle cx="6" cy="6" r="3.2" fill="none" stroke="#333333" stroke-width="0.8"/>
          <ellipse cx="6" cy="6" rx="1.4" ry="3.2" fill="none" stroke="#333333" stroke-width="0.7"/>
          <line x1="2.8" y1="6" x2="9.2" y2="6" stroke="#333333" stroke-width="0.7"/>
        </svg>
        <span>www.rustpawobedience.example</span>
      </li>
    </ul>
  </div>
</section>

</body>
</html>
```